Concierge Healthcare Business Card Design and Logo

We need a logo and business card design for a new company called "Sound Keeper". We will provide concierge audiological care, hearing aids, hearing exams, custom hearing protection etc to patients in the comfort of their homes and offices. We would like a sleek and modern design preferably with an Ear related logo.

Target Market(s)

People with hearing loss, Hunters, Musicians
My usual clientele are older individuals so usually 50+ years old

Industry/Entity Type

Health Care

Contact Information for Business Card

Clara Whitfield, AuD
Audiologist
512-418-2967
soundkeeper@mailvista.net
www.soundkeeperclinic.net

Logo Text

Sound Keeper

Number of Pages Required

3 page

```html
<!DOCTYPE html>
<html lang="en">
<head>
<meta charset="utf-8">
<title>Sound Keeper — Business Card</title>
<link rel="stylesheet" href="https://fonts.googleapis.com/css2?family=Mulish:wght@400;700&family=Questrial&display=swap">
<style>
  :root {
    --backdrop: #2b2c2b;
    --card-white: #f4f4f3;
    --card-white-edge: #ebebea;
    --brand-blue: #1a6bb8;
    --brand-blue-light: #1d74bd;
    --brand-blue-deep: #0a4778;
    --ink: #1f1f1f;
    --on-blue: #ffffff;
    --on-blue-soft: #e3ecf5;
  }
  * { margin: 0; padding: 0; box-sizing: border-box; }
  html, body {
    width: 1200px; height: 1200px; overflow: hidden;
    background: var(--backdrop);
  }
  .stage { position: relative; width: 1200px; height: 1200px; }

  .card {
    position: absolute; top: 445px;
    width: 505px; height: 294px;
    overflow: hidden;
  }

  /* Front: contact side */
  .card--front {
    left: 89px;
    background: radial-gradient(ellipse at 30% 20%, #fafaf9 0%, var(--card-white) 55%, var(--card-white-edge) 100%);
    font-family: "Questrial", sans-serif;
  }
  .holder {
    position: absolute; left: 26px; top: 98px;
  }
  .holder__name {
    font-family: "Mulish", sans-serif; font-weight: 700;
    font-size: 15px; color: var(--brand-blue); line-height: 1.1;
  }
  .holder__role {
    font-size: 12.5px; color: var(--ink); line-height: 1.2; margin-top: 1px;
  }
  .holder__rule {
    position: absolute; left: 25px; top: 139px;
    width: 161px; height: 1px; background: var(--brand-blue);
  }
  .contacts {
    position: absolute; left: 25px; top: 150px;
    list-style: none;
  }
  .contacts__item {
    display: flex; align-items: center; height: 21.5px;
    font-size: 13.2px; color: var(--ink);
  }
  .contacts__icon {
    width: 11px; height: 11px; margin-right: 7px; flex: none;
  }
  .contacts__accent { color: var(--brand-blue); }

  /* Back: brand side */
  .card--back {
    left: 607px;
    background: radial-gradient(ellipse 60% 70% at 50% 38%, var(--brand-blue-light) 0%, #155f9f 45%, var(--brand-blue-deep) 100%);
    font-family: "Mulish", sans-serif;
  }
  .wordmark {
    position: absolute; left: 0; right: 0; top: 128px;
    display: flex; justify-content: center; align-items: center; gap: 14px;
  }
  .wordmark__dot {
    width: 30px; height: 30px; border-radius: 50%;
    border: 2px solid var(--on-blue);
  }
  .wordmark__name {
    font-weight: 700; font-size: 37px; letter-spacing: 0.5px;
    color: var(--on-blue); line-height: 1;
  }
  .back__web {
    position: absolute; left: 0; right: 0; top: 256px;
    text-align: center;
    font-family: "Questrial", sans-serif;
    font-size: 13px; letter-spacing: 0.3px; color: var(--on-blue-soft);
  }
</style>
</head>
<body>
<main class="stage">

  <section class="card card--front" aria-label="Business card front">
    <div class="holder">
      <p class="holder__name">Clara Whitfield, AuD</p>
      <p class="holder__role">Audiologist</p>
    </div>
    <div class="holder__rule"></div>
    <ul class="contacts">
      <li class="contacts__item">
        <svg class="contacts__icon" viewBox="0 0 12 12" aria-hidden="true">
          <rect width="12" height="12" rx="1.5" fill="var(--brand-blue)"/>
          <path d="M3 4.2c0-.8 1.3-1.3 3-1.3s3 .5 3 1.3v.6H7.6v-.6H4.4v.6H3z M3.6 6h4.8v3H3.6z" fill="#fff"/>
        </svg>512-418-2967
      </li>
      <li class="contacts__item">
        <svg class="contacts__icon" viewBox="0 0 12 12" aria-hidden="true">
          <rect width="12" height="12" rx="1.5" fill="var(--brand-blue)"/>
          <rect x="2.5" y="3.5" width="7" height="5" fill="none" stroke="#fff" stroke-width="0.9"/>
          <path d="M2.5 3.5 6 6.3 9.5 3.5" fill="none" stroke="#fff" stroke-width="0.9"/>
        </svg>soundkeeper@mailvista.net
      </li>
      <li class="contacts__item">
        <svg class="contacts__icon" viewBox="0 0 12 12" aria-hidden="true">
          <rect width="12" height="12" rx="1.5" fill="var(--brand-blue)"/>
          <circle cx="6" cy="6" r="3.4" fill="none" stroke="#fff" stroke-width="0.8"/>
          <path d="M2.6 6h6.8M6 2.6c-1.6 2-1.6 4.8 0 6.8M6 2.6c1.6 2 1.6 4.8 0 6.8" fill="none" stroke="#fff" stroke-width="0.7"/>
        </svg>www.<span class="contacts__accent">soundkeeperclinic</span>.net
      </li>
    </ul>
  </section>

  <section class="card card--back" aria-label="Business card back">
    <div class="wordmark">
      <span class="wordmark__dot" aria-hidden="true"></span>
      <span class="wordmark__name">SOUND KEEPER</span>
    </div>
    <p class="back__web">www.soundkeeperclinic.net</p>
  </section>

</main>
</body>
</html>
```